Stationery and Logo Design Project for new NZ Accounting Firm

Our company name is based in Auckland, New Zealand and is called DHW CA Limited. We are a chartered accountancy firm hence the CA abbreviations.

We need a full logo stationery design: Logo, Letterhead, Business Card and Compliments slip.

We are looking for a bold, modern and clean/simple design that makes us stand out. We want to stand out as professionals in the industry and would like the logo and stationery that our clients see to convey this image. We also want to break away from the traditional boring views of book/bean accountants. We are not doing the same old things others are doing and are mainly cloud based but with face to face business relationship focused as well.

We see ourselves as business advisers that provide more than just filing their tax returns. We want to add value to their business and be a partner in their business ventures.

We want the logo to convey the above and also attract potential clients when they see our ads among the thousands on vornix and the civic atlas.

The logo can be for the "DHW" with CA Ltd seperately or a logo/design beside the DHW. But open to other suggestions or concept.

Hi Designers

The designs I have received so far is not quite what I want.

I want something modern and bold that is DIFFERENT from others, from the usual logo designs. Some logo that when people look at it they will remember it as opposed to fading in the background of other competitors' logo.

Lower case lettering for the DHW could be something to explore as I have not seen a lot of these and they do appeal to me.

Thanks

We can focus on the logo first as that will form the main part for all stationery.

Reason: Final stages of choosing a logo design so need to time for designers to submit the letterhead, namecards designs.

Our target clients are small to medium business ranging from the sole trader to 50 employees businesses

Business

```html
<!DOCTYPE html>
<html lang="en">
<head>
<meta charset="utf-8">
<title>DHW CA Ltd – Business Card</title>
<link rel="stylesheet" href="https://fonts.googleapis.com/css2?family=Exo+2:wght@400;600&display=swap">
<style>
  :root {
    --brand-orange: #f7941e;
    --text-grey: #808285;
    --card-border: #d4d4d4;
    --canvas-bg: #ffffff;
    --mark-faint: rgba(255, 255, 255, 0.32);
    --on-orange: #ffffff;
  }
  html, body {
    margin: 0;
    width: 1200px;
    height: 1000px;
    overflow: hidden;
    background: var(--canvas-bg);
    font-family: "Exo 2", sans-serif;
  }
  .canvas { position: relative; width: 1200px; height: 1000px; }

  .card {
    position: absolute;
    top: 348px;
    width: 489px;
    height: 303px;
    box-sizing: border-box;
  }
  .card--front { left: 77px; background: #fff; border: 2px solid var(--card-border); }
  .card--back { left: 637px; background: var(--brand-orange); }

  .wordmark {
    position: absolute;
    margin: 0;
    font-weight: 600;
    line-height: 1;
    white-space: nowrap;
    letter-spacing: -0.5px;
  }
  .card--front .wordmark { left: 24px; top: 96px; font-size: 50px; color: var(--brand-orange); }
  .card--back .wordmark { left: 262px; top: 206px; font-size: 40px; color: var(--mark-faint); }

  .identity {
    position: absolute;
    right: 29px;
    top: 44px;
    text-align: right;
  }
  .identity__name { margin: 0; font-size: 21px; font-weight: 600; color: var(--text-grey); line-height: 24px; }
  .identity__credentials { margin: 0; font-size: 14px; color: var(--brand-orange); line-height: 18px; }
  .identity__role { margin: 0; font-size: 17px; color: var(--text-grey); line-height: 24px; }

  .contact {
    position: absolute;
    left: 261px;
    top: 180px;
    margin: 0;
    padding: 0;
    list-style: none;
    font-size: 15px;
    line-height: 18.5px;
    color: var(--text-grey);
  }
  .contact__label {
    display: inline-block;
    width: 20px;
    font-weight: 600;
    color: var(--brand-orange);
  }

  .address {
    position: absolute;
    left: 27px;
    top: 38px;
    margin: 0;
    font-style: normal;
    font-size: 18px;
    line-height: 23px;
    color: var(--on-orange);
  }
</style>
</head>
<body>
<main class="canvas">
  <section class="card card--front" aria-label="Business card front">
    <p class="wordmark">DHW CA Ltd</p>
    <div class="identity">
      <p class="identity__name">Daniel Hart</p>
      <p class="identity__credentials">BCom, CA</p>
      <p class="identity__role">Director</p>
    </div>
    <ul class="contact">
      <li><span class="contact__label">E</span>daniel@dhw.co.nz</li>
      <li><span class="contact__label">M</span>021-437126</li>
      <li><span class="contact__label">P</span>0800 DHWCA LTD (349225)</li>
      <li><span class="contact__label">W</span>www.dhw.co.nz</li>
    </ul>
  </section>

  <section class="card card--back" aria-label="Business card back">
    <address class="address">
      418 Karaka Road<br>
      PO Box 52816<br>
      Kowhai Bay<br>
      Auckland 1152
    </address>
    <p class="wordmark">DHW CA Ltd</p>
  </section>
</main>
</body>
</html>
```